New Business Card Design For Re-Branded Company (New Logo)

We recently switched our DBA and had a new logo designed. We now need new business cards made around our new logo. We would like to stick with the color scheme in our logo: White, Orange, and Blue. We want to see original bold designs that reflect our position in the solar energy sector but we prefer simple over complicated.

We are curious about vertical designs so if you can translate your design onto a vertical layout we would be open to look at it. We especially like a few designs we have seen on here that are vertical with a black or very dark gray background. They have our logo on one side and then the normal vertical business card on the other side.

I have included a screenshot of one of the samples we like, labeled sample.jpg and a file we were given as an example of our logo on a dark background.

At the same time we are satisfied to stay with what we have always had in a horizontal format. If it's not a lot of extra work for you, designs that are submitted in both horizontal and vertical formats will be greatly appreciated.

Please submit your original, bold, clean designs for consideration. Contact us with any questions or comments that may arise.

Thank you and Good Luck,

KP

```html
<!DOCTYPE html>
<html lang="en">
<head>
<meta charset="utf-8">
<title>Kestrel Power – Business Card</title>
<link rel="stylesheet" href="https://fonts.googleapis.com/css2?family=Montserrat:wght@700&family=Open+Sans:wght@400;600&family=Roboto:wght@400;500&display=swap">
<style>
  :root {
    --bg: #d9d9d9;
    --white: #ececec;
    --blue: #1f73b7;
    --blue-dark: #0b4c94;
    --blue-light: #2a86c8;
    --orange: #e27a2e;
    --orange-dark: #c44f18;
    --text-soft: #f8e2d2;
    --edge: #141414;
  }
  * { margin: 0; padding: 0; box-sizing: border-box; }
  html, body { width: 1200px; height: 803px; overflow: hidden; background: var(--bg); }
  .stage { position: relative; width: 1200px; height: 803px; }
  .card {
    position: absolute;
    top: 132px;
    width: 332px;
    height: 572px;
    border: 2px solid var(--edge);
    border-radius: 3px;
    overflow: hidden;
    box-shadow: 0 0 0 6px #f2f2f2, 0 8px 18px rgba(0,0,0,.25);
  }
  .card--front { left: 244px; background: var(--white); }
  .card--back {
    left: 665px;
    background: linear-gradient(160deg, var(--blue-light) 0%, var(--blue) 45%, var(--blue-dark) 100%);
  }
  .card svg { display: block; }
  .brand-name { font-family: "Montserrat", sans-serif; font-weight: 700; font-size: 34px; fill: var(--blue); }
  .holder-name { font-family: "Open Sans", sans-serif; font-weight: 600; font-size: 29px; fill: #ffffff; letter-spacing: 1px; }
  .holder-role { font-family: "Roboto", sans-serif; font-weight: 500; font-size: 21px; fill: #ffffff; }
  .contact-line { font-family: "Roboto", sans-serif; font-weight: 400; font-size: 19px; fill: var(--text-soft); }
  .contact-small { font-family: "Roboto", sans-serif; font-weight: 400; font-size: 17.5px; fill: var(--text-soft); }
  .website {
    position: absolute;
    left: 0; right: 0;
    top: 514px;
    text-align: center;
    font-family: "Open Sans", sans-serif;
    font-size: 24px;
    letter-spacing: 1px;
    color: #e3ecf5;
  }
</style>
</head>
<body>
<main class="stage">
  <section class="card card--front" aria-label="Business card front">
    <svg width="328" height="568" viewBox="0 0 332 572">
      <defs>
        <linearGradient id="orangeFill" x1="1" y1="0" x2="0" y2="1">
          <stop offset="0" stop-color="var(--orange)"/>
          <stop offset="1" stop-color="var(--orange-dark)"/>
        </linearGradient>
        <path id="nameCurve" d="M0,249 Q166,321 332,249"/>
      </defs>

      <circle class="brand-mark" cx="166" cy="96" r="40" fill="none" stroke="var(--orange)" stroke-width="8"/>
      <text class="brand-name" x="166" y="194" text-anchor="middle">KESTREL POWER</text>

      <path class="band-orange" d="M0,268 Q166,340 332,268 L332,572 L0,572 Z" fill="url(#orangeFill)"/>
      <path class="band-blue" d="M0,230 Q166,302 332,230 L332,268 Q166,340 0,268 Z" fill="var(--blue)"/>
      <text class="holder-name"><textPath href="#nameCurve" startOffset="50%" text-anchor="middle">Marla Quinn</textPath></text>

      <text class="holder-role" x="166" y="331" text-anchor="middle">Managing Director</text>

      <g class="contact-icon" fill="var(--text-soft)">
        <rect x="82" y="394" width="15" height="13" rx="2"/>
        <rect x="82" y="422" width="15" height="13" rx="2"/>
        <rect x="82" y="450" width="15" height="13" rx="2"/>
      </g>
      <g fill="var(--orange-dark)">
        <path d="M85,398 h9 v2 h-2 l1,4 h-7 l1,-4 h-2 z"/>
        <path d="M86,425 q1,-1 2,0 l1,2 -1,1 q1,2 3,3 l1,-1 2,1 q1,1 0,2 q-4,1 -8,-8 z"/>
        <rect x="85" y="454" width="9" height="6"/>
      </g>
      <text class="contact-line" x="109" y="409">0412 305 118</text>
      <text class="contact-line" x="109" y="437">0412 774 260</text>
      <text class="contact-line" x="109" y="465">0412 305 119</text>

      <text class="contact-small" x="166" y="519" text-anchor="middle">marlaquinn@kestrelpower.com</text>
      <text class="contact-small" x="166" y="550" text-anchor="middle">1480 Ridge Oak Rd Conroe, TX 77301</text>
    </svg>
  </section>

  <section class="card card--back" aria-label="Business card back">
    <p class="website">www.kestrelpower.com</p>
  </section>
</main>
</body>
</html>
```